It's a fundraiser for Hand in Hand
A mentoring org that pairs college kids with learning disabilities with similar elementary and middle school kids. (Find out more at their website: handinhandnational.example.org)
We need to use their logo, and also kivora's logo-going to be a party atmosphere!
Sunday, June 1
10:30 AM-12:30
Penwick's restaurant, Millbrook, NY
$20 pp at door
$10 for kids
Updates
We are loving all the designs coming in for the Kivora fundraiser! We so appreciate everyone's time on this. A decision will be made by Wednesday-stay tuned!
I wanted to thank you all for submitting wonderful designs! It was very hard to decide, but alas, I had to choose only one. Thank you for your submissions!
Target Market(s)
All ages-no about dyslexia, or not, do Kivora or not
Industry/Entity Type
College

```html
<!DOCTYPE html>
<html lang="en">
<head>
<meta charset="utf-8">
<title>Hand in Hand Fundraiser</title>
<link rel="stylesheet" href="https://fonts.googleapis.com/css2?family=Abril+Fatface&family=Montserrat:wght@500;700&family=Oswald:wght@500&family=Pacifico&family=Poppins:wght@600;700&display=swap">
<style>
  :root {
    --teal: #1ba58d;
    --teal-light: #5fc5b4;
    --orange: #d9773d;
    --lime: #c9d84f;
    --salmon: #d9786c;
    --coral: #e4655a;
    --brown: #5a3517;
    --cream: #f4eedb;
    --gold: #f2a81d;
    --navy: #1d3a6b;
    --sky: #2aa2c9;
    --cloud: #e8f2f0;
    --violin: #e2d93b;
    --violin-deep: #cfc52e;
  }
  html, body { margin: 0; padding: 0; overflow: hidden; background: #ffffff; }
  .poster {
    position: relative; width: 960px; height: 1200px; overflow: hidden;
    background: var(--teal);
  }
  .backdrop, .art { position: absolute; inset: 0; width: 960px; height: 1200px; }
  .text { position: absolute; margin: 0; transform-origin: left top; white-space: nowrap; }
  .presenter {
    left: 285px; top: 70px; transform: rotate(-8deg);
    font-family: "Pacifico", cursive; font-size: 34px; color: var(--cream);
  }
  .title {
    left: 262px; top: 190px; transform: rotate(-8deg);
    font-family: "Poppins", sans-serif; font-weight: 600; font-size: 84px;
    letter-spacing: 1px; color: var(--cream); line-height: 1;
  }
  .subtitle {
    left: 300px; top: 300px; transform: rotate(-8deg);
    font-family: "Poppins", sans-serif; font-weight: 700; font-size: 86px;
    color: var(--gold); line-height: 1;
  }
  .event-details {
    left: 100px; top: 625px; transform: rotate(-5deg);
    font-family: "Oswald", sans-serif; font-weight: 500; color: var(--cream);
    font-size: 48px; line-height: 1.3;
  }
  .event-details .day { margin-left: 105px; }
  .venue {
    left: 100px; top: 838px; transform: rotate(-5deg);
    font-family: "Pacifico", cursive; font-size: 34px; color: var(--gold); line-height: 1.45;
  }
  .about {
    position: absolute; left: 535px; top: 462px; width: 380px; height: 196px;
    transform: rotate(-6deg); background: var(--cloud); border-radius: 60px;
    display: flex; flex-direction: column; justify-content: center; align-items: center;
    text-align: center; font-family: "Montserrat", sans-serif;
  }
  .about .mission { color: var(--orange); font-size: 14px; line-height: 1.35; margin: 0; }
  .about .extras { color: var(--sky); font-size: 14px; margin: 2px 0 0; }
  .about .invite { color: var(--sky); font-weight: 700; font-size: 21px; line-height: 1.2; margin: 6px 0 0; }
  .pricing {
    left: 630px; top: 712px; width: 300px; transform: rotate(-5deg);
    text-align: center; color: var(--navy); white-space: normal;
  }
  .pricing .amount { font-family: "Abril Fatface", serif; font-size: 104px; line-height: 1; margin: 0; }
  .pricing .label { font-family: "Abril Fatface", serif; font-size: 50px; line-height: 1.05; margin: 0 0 10px; }
  .info {
    left: 110px; top: 1018px; transform: rotate(-7deg);
    font-family: "Montserrat", sans-serif; color: var(--cream); text-align: center;
    font-size: 20px; line-height: 1.3; font-weight: 500;
  }
  .info .url, .info .sponsors { font-weight: 700; font-size: 21px; }
  .sponsor {
    position: absolute; top: 1112px; height: 76px; background: #ffffff;
    display: flex; align-items: center; justify-content: center; gap: 12px;
    font-family: "Poppins", sans-serif; font-weight: 600; color: var(--navy);
  }
  .sponsor.host { left: 142px; width: 250px; font-size: 28px; }
  .sponsor.partner { left: 415px; width: 86px; font-size: 17px; }
  .sponsor .mark { width: 30px; height: 30px; background: var(--sky); }
</style>
</head>
<body>
<main class="poster">
  <svg class="backdrop" viewBox="0 0 960 1200" aria-hidden="true">
    <polygon points="215,0 960,0 960,70 215,185" fill="var(--orange)"/>
    <polygon points="0,225 310,185 335,480 0,505" fill="var(--salmon)"/>
    <polygon points="300,420 960,330 960,415 320,505" fill="var(--lime)"/>
    <polygon points="500,460 960,400 960,760 530,770" fill="var(--teal-light)"/>
    <polygon points="0,505 110,490 90,600 0,610" fill="var(--coral)"/>
    <polygon points="500,680 960,630 960,1100 560,1150" fill="var(--lime)"/>
    <polygon points="0,900 560,870 590,1200 0,1200" fill="var(--salmon)"/>
    <polygon points="545,880 620,875 650,1170 585,1175" fill="var(--coral)"/>
    <polygon points="0,1095 600,1070 600,1200 0,1200" fill="var(--teal)"/>
  </svg>

  <svg class="art" viewBox="0 0 960 1200">
    <defs>
      <linearGradient id="violin-tone" x1="0" y1="0" x2="0" y2="1">
        <stop offset="0" stop-color="var(--violin)"/>
        <stop offset="1" stop-color="var(--violin-deep)"/>
      </linearGradient>
    </defs>
    <rect role="img" aria-label="Violin illustration" x="60" y="-30" width="160" height="470" rx="40"
          transform="rotate(-12 140 200)" fill="url(#violin-tone)"/>
    <polygon role="img" aria-label="Grand piano illustration" points="70,480 480,415 500,935 90,990" fill="var(--brown)"/>
  </svg>

  <p class="text presenter">your organization presents:</p>
  <h1 class="text title">HAND IN HAND</h1>
  <p class="text subtitle">FUNDRAISER</p>

  <div class="about">
    <p class="mission">A mentoring org<br>that pairs college kids<br>with learning disabilities with similar elementary<br>and<br>middle school kids.</p>
    <p class="extras">Food and Drinks will be available</p>
    <p class="invite">We hope<br>to see you there!</p>
  </div>

  <div class="text event-details">
    <div>SUNDAY, JUNE</div>
    <div class="day">1ST</div>
    <div>10:30 AM &gt; 12:30</div>
  </div>
  <div class="text venue">
    <div>Penwick's restaurant,</div>
    <div>Millbrook, NY</div>
  </div>

  <div class="text pricing">
    <p class="amount">$20</p>
    <p class="label">pp at door</p>
    <p class="amount">$10</p>
    <p class="label">for kids</p>
  </div>

  <div class="text info">
    <div>For more information please visit our website</div>
    <div class="url">handinhandnational.example.org</div>
    <div class="sponsors">sponsored by:</div>
  </div>

  <div class="sponsor host"><span class="mark"></span>Hand in Hand</div>
  <div class="sponsor partner">Kivora</div>
</main>
</body>
</html>
```